Catalogue Cover, spine and Divider pages

Design the cover, spine and divider pages for our first hard copy catalogue in line with the existing CD Cover design recently completed.

Cover size is 313mm h x 292mm w
Spine is 313mm h x 93mm w

Requirements
Must have
• Company Logo to front cover dividers and spine, design in line with recent CD Cover design, Web Address to front cover, Company name in full to front cover, 1300 toll free number to front cover.
Sample attached files are only a guide for the use of each section we would like a fresh approach in line with the recent CD cover design.

```html
<!DOCTYPE html>
<html lang="en">
<head>
<meta charset="utf-8">
<title>Meridian Architectural Systems – Divider Page</title>
<link href="https://fonts.googleapis.com/css2?family=Open+Sans:wght@600;700;800&display=swap" rel="stylesheet">
<style>
:root{
  --backdrop:#1c1c1c;
  --paper:#ffffff;
  --navy:#243a8c;
  --navy-dark:#1b2c6e;
  --orange:#e8552b;
  --tab-grey:#e4e6ea;
  --sky:#9cc3e6;
  --concrete:#b9bec4;
  --glass:#5a7fa8;
}
*{box-sizing:border-box;margin:0;padding:0}
html,body{width:1200px;height:1000px;overflow:hidden;background:var(--backdrop);font-family:"Open Sans",Arial,sans-serif}
.divider-page{position:absolute;left:300px;top:40px;width:580px;height:920px;background:var(--paper);border-radius:2px}
.section-tab{position:absolute;left:880px;top:60px;width:40px;height:120px;background:var(--paper);border-radius:0 10px 10px 0;display:flex;align-items:center;justify-content:center}
.section-tab span{writing-mode:vertical-rl;font-size:9px;font-weight:800;color:var(--navy);text-align:center;line-height:1.1;letter-spacing:.3px}
.brand{position:absolute;color:var(--navy);font-weight:800;line-height:1}
.brand .name{display:block;font-size:34px;letter-spacing:1px}
.brand .sub{display:block;font-size:12.5px;letter-spacing:.6px;margin-top:3px}
.brand-top{left:24px;top:40px}
.brand-grid{left:392px;top:712px;text-align:center}
.brand-grid .name{font-size:30px}
.brand-grid .sub{font-size:11px}
.product-tile{position:absolute;width:178px}
.product-photo{height:128px;border-radius:6px 6px 0 0}
.product-label{height:30px;background:var(--navy);border-radius:0 0 8px 8px;display:flex;align-items:center;padding:0 8px;gap:8px;color:#fff}
.product-code{color:var(--orange);font-weight:800;font-size:14px;min-width:26px}
.product-name{font-weight:700;font-size:10.5px;line-height:1.1;flex:1;text-align:center}
.photo-retail{background:linear-gradient(180deg,var(--sky) 0%,#c9d4dc 45%,#8d8f8c 100%)}
.photo-office{background:linear-gradient(180deg,#6d9fd4 0%,#d9dde0 50%,#7d8a78 100%)}
.photo-corner{background:linear-gradient(180deg,#cfd8e0 0%,#8fa6bd 50%,#c7ccd0 100%)}
.photo-warehouse{background:linear-gradient(180deg,#7fb2e6 0%,#e6e1d8 55%,#6f9c52 100%)}
.photo-brick{background:linear-gradient(135deg,#a4482c 0%,var(--glass) 45%,#c8d3de 100%)}
.photo-facade{background:linear-gradient(180deg,#5f93cf 0%,#b9c3c2 50%,#8a9a7e 100%)}
.photo-cafe{background:linear-gradient(180deg,#3e4a44 0%,#6d9a8a 50%,#3e6e3b 100%)}
.photo-blue{background:linear-gradient(180deg,#5a7fd0 0%,#5b4fa3 55%,#9a9d9c 100%)}
.photo-red{background:linear-gradient(135deg,#3f77c9 0%,#cf3a35 45%,#e2e4e6 100%)}
.photo-louvre{background:linear-gradient(180deg,#e7e7e4 0%,#cdcdc9 60%,#b9a48f 100%)}
.photo-subsill{background:linear-gradient(180deg,#7fb0e0 0%,#d8dcdc 50%,#8fa28a 100%)}
.tall .product-photo{height:168px}
</style>
</head>
<body>
  <div class="divider-page">
    <div class="brand brand-top"><span class="name">MERIDIAN</span><span class="sub">ARCHITECTURAL SYSTEMS</span></div>

    <div class="product-tile" style="left:18px;top:120px">
      <div class="product-photo photo-retail" role="img" aria-label="Photo of a retail building with centre glazed shopfront"></div>
      <div class="product-label"><span class="product-code">C1</span><span class="product-name">101.6mm Centre Glaze</span></div>
    </div>
    <div class="product-tile" style="left:201px;top:120px">
      <div class="product-photo photo-office" role="img" aria-label="Photo of a two storey office with centre glazing"></div>
      <div class="product-label"><span class="product-code">C2</span><span class="product-name">150mm Centre Glaze</span></div>
    </div>
    <div class="product-tile" style="left:384px;top:120px">
      <div class="product-photo photo-corner" role="img" aria-label="Photo of a glazed building corner"></div>
      <div class="product-label"><span class="product-code">C3</span><span class="product-name">100mm Front Glazed</span></div>
    </div>

    <div class="product-tile" style="left:18px;top:296px">
      <div class="product-photo photo-warehouse" role="img" aria-label="Photo of an industrial unit with landscaping"></div>
      <div class="product-label"><span class="product-code">C4</span><span class="product-name">150 Front Glazed</span></div>
    </div>
    <div class="product-tile" style="left:201px;top:296px">
      <div class="product-photo photo-brick" role="img" aria-label="Photo of a multi storey brick and glass building"></div>
      <div class="product-label"><span class="product-code">C5</span><span class="product-name">150 Stackable Front Glazed</span></div>
    </div>
    <div class="product-tile" style="left:384px;top:296px">
      <div class="product-photo photo-facade" role="img" aria-label="Photo of an office facade with double front glazing"></div>
      <div class="product-label"><span class="product-code">C6</span><span class="product-name">100mm Double Front Glazed</span></div>
    </div>

    <div class="product-tile" style="left:18px;top:472px">
      <div class="product-photo photo-cafe" role="img" aria-label="Photo of an interior with floor to ceiling glazing"></div>
      <div class="product-label"><span class="product-code">C7</span><span class="product-name">150mm Double Front Glazed</span></div>
    </div>
    <div class="product-tile" style="left:201px;top:472px">
      <div class="product-photo photo-blue" role="img" aria-label="Photo of a blue glazed office building"></div>
      <div class="product-label"><span class="product-code">C8</span><span class="product-name">150mm Stackable Double Front Glazed</span></div>
    </div>
    <div class="product-tile" style="left:384px;top:472px">
      <div class="product-photo photo-red" role="img" aria-label="Photo of a building with red panels and commercial door"></div>
      <div class="product-label"><span class="product-code">C9</span><span class="product-name">45mm Commercial Door</span></div>
    </div>

    <div class="product-tile tall" style="left:18px;top:650px;width:232px">
      <div class="product-photo photo-louvre" role="img" aria-label="Photo of a fixed louvre screen on a wall"></div>
      <div class="product-label"><span class="product-code">C10</span><span class="product-name">Fixed Louvre</span></div>
    </div>
    <div class="brand brand-grid"><span class="name">MERIDIAN</span><span class="sub">ARCHITECTURAL SYSTEMS</span></div>
    <div class="product-tile tall" style="left:270px;top:650px;width:110px;display:none"></div>
    <div class="product-tile tall" style="left:384px;top:650px">
      <div class="product-photo photo-subsill" role="img" aria-label="Photo of an office building with subheads and subsills"></div>
      <div class="product-label"><span class="product-code">C11</span><span class="product-name">Subhead and Subsills</span></div>
    </div>
  </div>
  <div class="section-tab"><span>MERIDIAN<br>ARCHITECTURAL<br>SYSTEMS</span></div>
</body>
</html>
```